label redesign for skincare product

We would like a redesign of existing labels for a skincare product that we make (the existing labels are attached). This is a very natural product, but the existing labels are not right - one of the labels wraps around the jar, and one of the labels is placed on the bottom of the jar (copies of these attached). It needs softening and to be made less brutal looking. The label needs to communicate luxury quality product, that contains natural products, whilst maintaining a contemporary feel. The audience is male and female.

The product is called 'Dew Haven' and our company is called RB Naturals. We have a website at www.rbnaturals-example.com where the existing product can be seen. It is NOT however necessary for the RB Naturals logo from the website to be used on the label - this is at the discretion of the designer.

The packaging will remain the same - this is a glass jar in extremely deep purple, almost black.

The colour of the product inside the jar is off white. The product contain mandarin and geranium essential oils so is floral and citrussy smelling.

Target Market(s)

Adults who like high quality natural skincare products, 30-65.

Industry/Entity Type

It Company

Font styles to use
Serif
Sans Serif

Colors

Designer to choose colors to be used in the design.

Requirements
Must have
• The long label must by 13mm high and 110 mm wide. The round label for the back of the jar must be 40mm diameter..

```html
<!DOCTYPE html>
<html lang="en">
<head>
<meta charset="utf-8">
<title>RB Naturals – Dew Haven jar label</title>
<link rel="stylesheet" href="https://fonts.googleapis.com/css2?family=Arimo:wght@400;700&display=swap">
<style>
  :root {
    --backdrop: #3f6479;
    --label-white: #ffffff;
    --panel-tan: #b89c7c;
    --edge-gold: #d9b77e;
    --ink-brown: #3b2b23;
    --ink-grey: #5a5a5a;
    --ink-dark: #444444;
    --rule: #7a7a7a;
    --panel-text: #ffffff;
  }
  * { margin: 0; padding: 0; box-sizing: border-box; }
  html, body {
    width: 1200px;
    height: 1000px;
    overflow: hidden;
    background: var(--backdrop);
    font-family: "Arimo", Arial, sans-serif;
  }
  .label {
    position: absolute;
    left: 50px;
    top: 390px;
    width: 1100px;
    height: 220px;
    background: var(--label-white);
    overflow: hidden;
  }
  .label__panel-shape {
    position: absolute;
    inset: 0;
    width: 1100px;
    height: 220px;
  }
  .brand-name {
    position: absolute;
    left: 68px;
    top: 28px;
    font-size: 30px;
    font-weight: 400;
    letter-spacing: -0.5px;
    color: var(--ink-dark);
    text-transform: uppercase;
  }
  .product-title {
    position: absolute;
    left: 64px;
    top: 62px;
    font-size: 88px;
    line-height: 1;
    letter-spacing: -1px;
    white-space: nowrap;
  }
  .product-title__strong { font-weight: 700; color: var(--ink-brown); }
  .product-title__light { font-weight: 400; color: var(--ink-grey); }
  .title-rule {
    position: absolute;
    left: 64px;
    top: 152px;
    width: 545px;
    height: 2px;
    background: var(--rule);
  }
  .product-description {
    position: absolute;
    left: 64px;
    top: 160px;
    width: 560px;
    font-size: 18px;
    line-height: 22px;
    color: var(--ink-dark);
  }
  .usage-panel {
    position: absolute;
    left: 670px;
    top: 30px;
    width: 410px;
    text-align: center;
    color: var(--panel-text);
    font-size: 16px;
    line-height: 24px;
  }
  .usage-panel__address { margin-top: 16px; }
</style>
</head>
<body>
  <div class="label">
    <svg class="label__panel-shape" viewBox="0 0 1100 220" aria-hidden="true">
      <path d="M700 0 C665 60 640 150 625 220 L1100 220 L1100 0 Z" fill="var(--panel-tan)"/>
      <path d="M700 0 C665 60 640 150 625 220" fill="none" stroke="var(--edge-gold)" stroke-width="6"/>
    </svg>

    <div class="brand-name">RB Naturals</div>
    <h1 class="product-title"><span class="product-title__strong">DEW</span><span class="product-title__light">HAVEN</span></h1>
    <div class="title-rule"></div>
    <p class="product-description">RB Naturals Dew Haven with Calendula, Green Mandarin and Geranium.</p>

    <div class="usage-panel">
      <p>Moisturing salve for dry skin with natural oils.<br>
      Apply to dry skin that needs soothing as required.<br>
      For external use only. Test on a small area first.<br>
      Whilst unlikely, if you experience irritation, stop use<br>
      and consult a doctor. Store in a cool dry place.</p>
      <p class="usage-panel__address">RB Naturals, 14 Meadow Row, London</p>
    </div>
  </div>
</body>
</html>
```